Re-brand our business and design!

We need a simple informational website (editable for in the future use)
We need our logo(we have included logo), name, who we are, and what we do displayed.

This is our current site (which is not acceptable, and only a template site): all our information is on this site, please use it forreferanceofinformation.
Www.brightlanefixers.com

Target Market(s)

Real estate brokers, and realtors,homeowners, and anyone looking for home repairs.

Industry/Entity Type

Business

Number of Pages Required

4 page

Font styles to use
Sans Serif

Requirements
Must have
• Our name, contact info, services, and our logo (which we will Email upon request)
• MUST have originality to the site.
• custom "contact us form" or request an estimate form.
Nice to have
• page for real customer testimonies.
• page for our previous work where we can upload pics of completed jobs.
Should not have
• any infringements on any copyrights or plagiarism at all.

```html
<!DOCTYPE html>
<html lang="en">
<head>
<meta charset="utf-8">
<title>Bright Lane Fixers – Home Repairs and Maintenance</title>
<link href="https://fonts.googleapis.com/css2?family=Open+Sans:wght@400;600;700&display=swap" rel="stylesheet">
<style>
:root{
  --red:#e8141b;
  --ink:#1c1c1c;
  --text:#555;
  --grey:#8a8a8a;
  --footer:#2f2f2f;
  --footer-bottom:#454545;
  --white:#fff;
}
*{margin:0;padding:0;box-sizing:border-box}
html,body{width:710px;height:1200px;overflow:hidden;background:var(--white)}
body{position:relative;font-family:"Open Sans",Arial,sans-serif;color:var(--text)}
.abs{position:absolute}

/* header */
.site-header{position:absolute;left:0;top:0;width:710px;height:80px;border-top:1px solid #222}
.brand{left:35px;top:22px;display:flex;align-items:center;gap:7px}
.brand-mark{width:12px;height:12px;background:var(--red)}
.brand-name{font-weight:700;font-size:15px;color:var(--ink);line-height:1.05}
.brand-name small{display:block;font-size:15px}
.call-tab{left:490px;top:0;width:175px;height:20px;background:var(--ink);border-radius:0 0 12px 12px;display:flex;font-size:8px;color:var(--white);align-items:center}
.call-tab .label{padding-left:14px;width:92px;display:flex;align-items:center;gap:4px}
.call-tab .phone{background:var(--red);height:20px;flex:1;border-radius:0 0 12px 12px;display:flex;align-items:center;gap:4px;padding-left:10px;font-weight:700;font-size:8.5px}
.main-nav{right:21px;top:44px;display:flex;gap:24px;font-size:9.5px;font-weight:600;color:var(--ink);letter-spacing:.2px}
.main-nav .active{color:var(--red)}

/* hero */
.hero{left:0;top:80px;width:710px;height:300px;background:linear-gradient(160deg,#3b4a5c 0%,#4d5868 40%,#7a4b3c 70%,#a3453e 100%)}

/* intro */
.intro{left:0;top:405px;width:710px;text-align:center}
.intro h1{font-size:24px;font-weight:600;color:var(--ink)}
.intro p{width:600px;margin:12px auto 0;font-size:8.5px;line-height:14px}
.btn{display:inline-block;background:var(--red);color:var(--white);font-size:8px;font-weight:700;border-radius:11px;width:117px;height:22px;line-height:22px;margin-top:20px}

/* services */
.spine{left:354px;top:569px;width:10px;height:360px;background:#7d7d7d;border-radius:5px}
.spine-dot{left:353px;width:12px;height:12px;border-radius:50%;background:#7d7d7d;border:2px solid var(--white)}
.service-icon{width:78px;height:78px;border-radius:50%;background:var(--red);border:3px solid #9a9a9a;display:flex;align-items:center;justify-content:center}
.service{width:210px}
.service h3{font-size:11px;font-weight:600;color:var(--ink);margin-bottom:6px}
.service p{font-size:7.5px;line-height:14px}
.service.left{text-align:right}

/* footer */
.site-footer{left:0;top:995px;width:710px;height:180px;background:var(--footer);color:var(--white)}
.footer-brand{left:37px;top:45px;font-weight:700;font-size:11px;line-height:1.1;display:flex;align-items:center;gap:6px}
.footer-brand .brand-mark{width:10px;height:10px}
.footer-about{left:36px;top:87px;width:170px;font-size:8px;line-height:10.5px;color:#ddd}
.footer-head{font-size:11.5px;font-weight:600;letter-spacing:.2px}
.footer-nav{left:225px;top:50px;font-size:7.5px;font-weight:700;list-style:none}
.footer-nav li{height:19.7px}
.footer-nav li.active{color:var(--red);font-weight:400}
.contact-row{display:flex;gap:10px;font-size:7.5px;line-height:10px}
.contact-ico{width:16px;height:16px;border-radius:50%;background:var(--red);flex:none;display:flex;align-items:center;justify-content:center}
.newsletter p{font-size:8px;line-height:14px;color:#ddd;margin-top:12px}
.email-field{margin-top:12px;width:171px;height:28px;border:1px solid #888;font-size:7.5px;padding:0 8px;line-height:26px}
.signup{margin-top:12px;width:171px;height:27px;background:var(--red);text-align:center;font-size:8px;font-weight:700;line-height:27px}
.copyright{left:0;top:1175px;width:710px;height:25px;background:var(--footer-bottom);color:var(--white);font-size:7px;text-align:center;line-height:25px}
</style>
</head>
<body>

<header class="site-header">
  <div class="abs brand"><span class="brand-mark"></span><span class="brand-name">Bright Lane Fixers<small>And Maintenance</small></span></div>
  <div class="abs call-tab">
    <span class="label"><svg width="8" height="8" viewBox="0 0 10 10"><circle cx="5" cy="3" r="2.5" fill="#fff"/><path d="M0 10a5 4 0 0 1 10 0z" fill="#fff"/></svg>CALL US NOW</span>
    <span class="phone"><svg width="8" height="8" viewBox="0 0 10 10"><path d="M2 0l2 2.5-1.2 1.3a6 6 0 0 0 3.4 3.4L7.5 6 10 8 8.5 10C4 10 0 6 0 1.5z" fill="#fff"/></svg>555-014-2290</span>
  </div>
  <nav class="abs main-nav"><span class="active">HOME</span><span>PAGES</span><span>SERVICES</span><span>BLOG</span><span>GALLERY</span><span>CONTACT US</span></nav>
</header>

<div class="abs hero" role="img" aria-label="Photo of a repairman on a ladder cleaning the gutter of a shingled house roof"></div>

<section class="abs intro">
  <h1>Who we are</h1>
  <p>Lorem Ipsum is simply dummy text of the printing and typesetting industry. Lorem Ipsum has been the industry's standard dummy text ever since the 1500s, when an unknown printer took a galley of type and scrambled it to make a type specimen book</p>
  <span class="btn">READ MORE</span>
</section>

<div class="abs spine"></div>
<div class="abs spine-dot" style="top:617px"></div>
<div class="abs spine-dot" style="top:748px"></div>
<div class="abs spine-dot" style="top:872px"></div>

<!-- left column -->
<div class="abs service left" style="left:18px;top:592px"><h3>Roofing Maintance</h3><p>Painting, Pressure/Power washing<br>Heavy lifting, Property Clean OutsMinor RepairsVinyl Siding, Gutters, Clean and seal tile, Caulking, Patch and repair drywall, replace hard to reach light bulbs, Painting, Cosmetic repair, Debris removal.</p></div>
<div class="abs service left" style="left:16px;top:719px"><h3>Plumbing</h3><p>Bathrooms, Kitchens, Washer/Dryer Hook Up<br>Clogged drains, Toilets, Tubs/Showers<br>Sinks, Garbage disposals, Leaking faucets vent</p></div>
<div class="abs service left" style="left:16px;top:846px"><h3>Carpentry</h3><p>Stairs, Floors, Decks, Fences<br>Storage sheds, Storage shelving and doors<br>Vapor barrier repair/installation, Attic and crawl space,</p></div>

<!-- icons -->
<div class="abs service-icon" style="left:243px;top:583px"><svg width="40" height="40" viewBox="0 0 40 40"><path d="M4 20L20 6l16 14" fill="none" stroke="#fff" stroke-width="3.5" stroke-linejoin="round"/><circle cx="20" cy="21" r="4" fill="#fff"/><rect x="14" y="26" width="12" height="9" rx="2" fill="#fff"/></svg></div>
<div class="abs service-icon" style="left:243px;top:717px"><svg width="42" height="42" viewBox="0 0 42 42"><rect x="6" y="10" width="20" height="6" fill="#fff"/><rect x="13" y="6" width="6" height="4" fill="#fff"/><rect x="9" y="4" width="14" height="3" fill="#fff"/><path d="M24 14h12v12h-6v-6h-6z" fill="#fff"/><rect x="30" y="28" width="6" height="3" fill="#fff"/></svg></div>
<div class="abs service-icon" style="left:243px;top:836px"><svg width="40" height="40" viewBox="0 0 40 40"><path d="M8 30L28 8l5 5-20 22z" fill="#fff"/><rect x="3" y="27" width="10" height="8" transform="rotate(-45 8 31)" fill="#fff"/></svg></div>
<div class="abs service-icon" style="left:389px;top:585px"><svg width="40" height="40" viewBox="0 0 40 40"><path d="M11 8h18v24H11z" fill="none" stroke="#fff" stroke-width="2.5"/><path d="M11 8l10 4v24l-10-4z" fill="#fff"/></svg></div>
<div class="abs service-icon" style="left:389px;top:716px"><svg width="40" height="40" viewBox="0 0 40 40"><path d="M8 34L24 14" stroke="#fff" stroke-width="3" stroke-linecap="round"/><path d="M18 12l8-6 8 8-4 2-4-2-4 4z" fill="#fff"/></svg></div>
<div class="abs service-icon" style="left:389px;top:840px"><svg width="40" height="40" viewBox="0 0 40 40"><path d="M14 10l16 16-6 4-14-14z" fill="none" stroke="#fff" stroke-width="2.5"/><path d="M10 18l-6-6M16 12l-6-6M26 28l6 8" stroke="#fff" stroke-width="2.5" stroke-linecap="round"/></svg></div>

<!-- right column -->
<div class="abs service" style="left:480px;top:592px"><h3>Doors and Windows</h3><p>Weatherstripping, Replacements<br>Glass and Screen Installation and Repair, Install locksets</p></div>
<div class="abs service" style="left:481px;top:718px"><h3>Small Construction</h3><p>Stairs, Floors, Decks, Fences Storage sheds,Storage shelves<br>Masonry</p></div>
<div class="abs service" style="left:479px;top:844px;width:190px"><h3>Electrical</h3><p>Bright Lane Fixers has licensed electricians who can rewire your entire house, or just a GFCI. We can respond to your electrical needs quickly. Code/Service Upgrades Fuses and Circuit Breakers Recessed Lighting Ceiling Fixtures</p></div>

<footer class="abs site-footer">
  <div class="abs footer-brand"><span class="brand-mark"></span><span>Bright Lane Fixers<br>And Maintenance</span></div>
  <p class="abs footer-about">Serving the Maple Ridge, and surrounding areas.<br>One Name, One number, One call means one service for fast timely quotes, home repairs and updates for you and/or your clients.</p>

  <div class="abs footer-head" style="left:226px;top:23px">NAVIGATION</div>
  <ul class="abs footer-nav"><li class="active">HOME</li><li>PAGES</li><li>SERVICES</li><li>BLOG</li><li>GALLERY</li><li>CONTACT US</li></ul>

  <div class="abs" style="left:339px;top:23px">
    <div class="footer-head">CONTACT DETAILS</div>
    <div class="contact-row" style="margin-top:15px"><span class="contact-ico"><svg width="8" height="10" viewBox="0 0 8 10"><path d="M4 10L1 5a3.5 3.5 0 1 1 6 0z" fill="#fff"/><circle cx="4" cy="3.6" r="1.3" fill="#e8141b"/></svg></span><span><b>LANEFIELD WORKS</b><br>Diam nummy Rich,<br>eulioumm tincidunt ut laor<br>laoreet dolore magna<br>123456</span></div>
    <div class="contact-row" style="margin-top:6px"><span class="contact-ico"><svg width="8" height="8" viewBox="0 0 10 10"><path d="M2 0l2 2.5-1.2 1.3a6 6 0 0 0 3.4 3.4L7.5 6 10 8 8.5 10C4 10 0 6 0 1.5z" fill="#fff"/></svg></span><span style="line-height:16px">555-014-2290</span></div>
    <div class="contact-row" style="margin-top:9px"><span class="contact-ico"><svg width="9" height="7" viewBox="0 0 9 7"><rect width="9" height="7" fill="#fff"/><path d="M0 0l4.5 4L9 0" fill="none" stroke="#e8141b"/></svg></span><span style="line-height:16px">sam@brightlanefixers.com</span></div>
  </div>

  <div class="abs newsletter" style="left:503px;top:27px">
    <div class="footer-head">SUBSCRIBE NEWSLETTER</div>
    <p>Enter your email address for our mailing list to keep your self our latest updated.</p>
    <div class="email-field">Email Address</div>
    <div class="signup">SIGN UP</div>
  </div>
</footer>
<div class="abs copyright">Copyright © 2007 - 2016 BRIGHT LANE FIXERS All Rights Reserved</div>

</body>
</html>
```